Boutique Jewellery Card [UPDATED] Embossing and Foil

Hi Designers,

What will win you this competition is your input on making my card look very professional and classy

Just some overview information.

I am striving to be the most prestigious jeweller going around specialising in custom designed jewellery, engagement rings and repairs on a bigger budget.

I am spending a lot on the printing including thick cards, rounded corners, multi level embossing and foiling.

Front:

I want my entire logo on the front, which I will have embossed and foiled (source file included)
Optional: I also want a lower embossing of a repeating pattern which I am not sure on. I need YOUR input here

Back:

I need you to use your skills and experience to make my details look very important, professional and classy.

The details I need on the back are:

Marcus Delvaney
Your Jewellery Stylist

www.marcusdelvaney.com
0492 836 514
marcus@marcusdelvaney.com

The font MUST match the font/style used in the logo.
Everything else including layout, whether my logo is on the back etc, engrave/endent, foiling etc is what I need your input for
Updates

Project Deadline Extended Reason: I was a bit slow and out of action at the start, but we're almost there, just need a few more days to finalize Added Sunday, November 16, 2014

Target Market(s)

25 - 80 year olds. Fashion concious. Wealthy

Industry/Entity Type

Printing

Contact Information for Business Card

Marcus Delvaney
Your Jewellery Stylist

0492 836 514
marcus@marcusdelvaney.com
www.marcusdelvaney.com
- facebook and instagram logo's

Requirements
Must have
• Must use the font from my logo on the back, or very similar
• My logo on the front
• My details on the back must be the centre of attention, my logo can still be there but is less important.
• Back must include the facebook and instagram logo's
Nice to have
• repeating pattern or monogram

```html
<!DOCTYPE html>
<html lang="en">
<head>
<meta charset="utf-8">
<title>Marcus Delvaney – Business Card Print Spec</title>
<link rel="stylesheet" href="https://fonts.googleapis.com/css2?family=Arimo:wght@400;700&display=swap">
<style>
  :root {
    --sheet: #ffffff;
    --label: #000000;
    --card: #262626;
    --trim-line: #3d3d3d;
    --foil: #0d0d0d;
    --leader: #000000;
  }
  * { box-sizing: border-box; margin: 0; padding: 0; }
  html, body { width: 953px; height: 1200px; overflow: hidden; background: var(--sheet); }
  body { position: relative; font-family: "Arimo", Arial, sans-serif; color: var(--label); }

  .spec-title, .side-title, .callout, .swatch-label {
    position: absolute; font-weight: 700; white-space: nowrap;
  }
  .spec-title { font-size: 22px; left: 93px; }
  .side-title { font-size: 18px; transform: translateX(-50%); }

  .card {
    position: absolute; left: 0; width: 607px;
    background: var(--card); border-radius: 21px;
  }
  .card--front { top: 110px; height: 388px; }
  .card--back { top: 814px; height: 386px; border-radius: 21px 21px 0 21px; }

  .trim-line {
    position: absolute; left: 18px; right: 19px;
    border: 1.5px solid var(--trim-line); border-radius: 18px;
  }
  .card--front .trim-line { top: 18px; bottom: 19px; }
  .card--back .trim-line { top: 18px; bottom: 17px; }

  .foil-swatch { position: absolute; width: 65px; height: 65px; background: var(--foil); }
  .swatch-label { font-size: 18px; }

  .leader { position: absolute; height: 1.5px; background: var(--leader); }
  .callout { font-size: 18px; transform: translateY(-50%); }

  .brand-mark {
    position: absolute; border: 9px solid var(--foil); border-radius: 50%;
  }
  .brand-name {
    position: absolute; left: 0; right: 0; text-align: center;
    color: var(--foil); font-weight: 400; letter-spacing: 0.22em; font-size: 34px;
  }

  .details { position: absolute; left: 0; right: 0; text-align: center; color: var(--foil); }
  .details__name { font-size: 25px; font-weight: 700; }
  .details__role { font-size: 17px; margin-top: 6px; }
  .details__contact { font-size: 16px; line-height: 24px; margin-top: 18px; }
</style>
</head>
<body>

  <!-- Front -->
  <h1 class="spec-title" style="top:4px;">Business Card -&nbsp; (w)90mm X (h)55mm</h1>
  <h2 class="side-title" style="left:302px; top:54px;">Front</h2>

  <section class="card card--front" aria-label="Card front">
    <div class="trim-line"></div>
    <div class="brand-mark" style="left:230px; top:89px; width:144px; height:144px;"></div>
    <p class="brand-name" style="top:240px;">MARCUS DELVANEY</p>
  </section>

  <div class="foil-swatch" style="left:629px; top:113px;"></div>
  <p class="swatch-label" style="left:707px; top:134px;">Embossed gloss black foil</p>

  <div class="leader" style="left:594px; top:394px; width:74px;"></div>
  <p class="callout" style="left:670px; top:395px;">Trim Size</p>
  <div class="leader" style="left:607px; top:471px; width:61px;"></div>
  <p class="callout" style="left:670px; top:472px;">Bleed Size</p>

  <!-- Back -->
  <h1 class="spec-title" style="top:706px;">Business Card -&nbsp; (w)90mm X (h)55mm</h1>
  <h2 class="side-title" style="left:302px; top:758px;">Back</h2>

  <section class="card card--back" aria-label="Card back">
    <div class="trim-line"></div>
    <div class="brand-mark" style="left:262px; top:67px; width:90px; height:90px; border-width:7px;"></div>
    <div class="details" style="top:170px;">
      <p class="details__name">Marcus Delvaney</p>
      <p class="details__role">Your Jewellery Stylist</p>
      <p class="details__contact">0492 836 514<br>marcus@marcusdelvaney.com<br>www.marcusdelvaney.com</p>
    </div>
  </section>

  <div class="foil-swatch" style="left:632px; top:817px;"></div>
  <p class="swatch-label" style="left:710px; top:836px;">Embossed gloss black foil</p>

  <div class="leader" style="left:594px; top:1099px; width:76px;"></div>
  <p class="callout" style="left:672px; top:1100px;">Trim Size</p>
  <div class="leader" style="left:607px; top:1174px; width:63px;"></div>
  <p class="callout" style="left:672px; top:1175px;">Bleed Size</p>

</body>
</html>
```